Word Press Website design

Harborlight Studio is a Website design, SEO, Social Networking and app development company. We would like to see what you can do to create a new, relevant and exciting design for us. This is our first project for Pixel Meadow so we thought we would test drive this site.  We would like to leave it up to your creative interpretation of the new design, but you can checkout our old design at www.harborlightstudiohub.example
We are always looking for new talent for future projects. Wow us with your designs and there will be future work for you.

Target Market(s)
Our target customers are medium sized businesses of all vertical markets.
Industry/Entity Type
Internet
Font styles to use
Requirements
Must have
- Easy to navigate, HTML 5 sliders, modern
Nice to have
- Bring your graphic talents with an outside of the box design that will standout to prospective clients.

```html
<!DOCTYPE html>
<html lang="en">
<head>
<meta charset="utf-8">
<title>Harborlight Studio – Website Design Services</title>
<link href="https://fonts.googleapis.com/css2?family=Raleway:wght@500;600;700&family=Open+Sans:wght@400;600;700&display=swap" rel="stylesheet">
<style>
:root{
  --red:#e4262c;
  --ink:#1d1d1d;
  --text:#666;
  --muted:#8a8a8a;
  --icon-grey:#555;
  --band:#f1f1f1;
  --card-bar:#3b3b3b;
  --line:#d9d9d9;
  --footer:#23272c;
  --white:#fff;
}
*{box-sizing:border-box;margin:0;padding:0}
html,body{width:1200px;height:3025px;overflow:hidden}
body{position:relative;background:var(--white);font-family:'Open Sans',Arial,sans-serif;color:var(--text)}
.abs{position:absolute}
h1,h2,h3{font-family:'Raleway',Arial,sans-serif;color:var(--ink)}
.section-title{position:absolute;left:0;width:1200px;text-align:center;font-size:40px;font-weight:600}
.section-intro{position:absolute;left:140px;width:920px;text-align:center;font-size:12.5px;line-height:22px;color:var(--muted)}

/* header */
.site-header{position:absolute;top:0;left:0;width:1200px;height:100px;background:var(--white)}
.brand{position:absolute;left:110px;top:30px;display:flex;align-items:center;gap:12px}
.brand-mark{width:36px;height:36px;background:var(--ink)}
.brand-name{font-family:'Open Sans',Arial,sans-serif;font-weight:700;font-size:22px;color:var(--ink)}
.main-nav a{position:absolute;top:40px;font-size:15px;color:#444;text-decoration:none}
.main-nav a.active{color:var(--red);font-weight:600}
.nav-underline{position:absolute;left:546px;top:94px;width:66px;height:4px;background:var(--red)}

/* hero */
.hero{position:absolute;top:100px;left:0;width:1200px;height:545px;
  background:linear-gradient(180deg,#f4ede6 0%,#efe6dc 60%,#e4d8cc 100%)}
.hero-title{position:absolute;top:138px;left:0;width:1200px;text-align:center;font-size:40px;font-weight:700}
.hero-sub{position:absolute;top:190px;left:220px;width:760px;text-align:center;font-size:19px;line-height:28px;color:#555}
.hero-photo{position:absolute;left:290px;top:275px;width:560px;height:370px;border-radius:14px 14px 0 0;
  background:linear-gradient(160deg,#2b2b2b 0%,#3d3d3d 50%,#d9b9a0 100%)}

/* services */
.service{position:absolute;top:848px;width:240px;text-align:center}
.service .badge{width:122px;height:122px;border-radius:50%;margin:0 auto;display:flex;align-items:center;justify-content:center}
.badge.red{background:var(--red)}
.badge.grey{background:var(--icon-grey)}
.service h3{font-size:18px;font-weight:500;margin-top:26px}
.service p{font-size:11.5px;line-height:20px;color:var(--muted);margin-top:14px;padding:0 10px}

/* work */
.work-band{position:absolute;top:1160px;left:0;width:1200px;height:680px;background:var(--band)}
.work-card{position:absolute;top:1388px;width:246px;height:383px;background:var(--white);box-shadow:0 1px 3px rgba(0,0,0,.08)}
.work-card .shot{height:196px}
.work-card .label{height:36px;background:var(--card-bar);color:var(--white);font-size:14.5px;font-weight:600;text-align:center;line-height:36px}
.work-card .label.featured{background:var(--red)}
.work-card p{font-size:10px;line-height:16px;color:var(--muted);text-align:center;padding:16px 14px 0}
.share{position:absolute;left:0;right:0;bottom:20px;display:flex;justify-content:center;gap:2px}
.share span{width:22px;height:22px}
.s1{background:#3b5998}.s2{background:#333}.s3{background:#2ea7df}.s4{background:#1fa4d8}

/* about */
.about-stem{position:absolute;left:598px;top:1840px;width:4px;height:26px;background:var(--red)}
.about-badge{position:absolute;left:543px;top:1859px;width:114px;height:114px;border-radius:50%;background:var(--red);
  box-shadow:0 0 0 6px rgba(228,38,44,.12);display:flex;align-items:center;justify-content:center}
.about-visual{position:absolute;left:111px;top:2148px;width:343px;height:212px;
  background:radial-gradient(ellipse at 55% 60%,#cfeaf7 0%,#e9f4fa 45%,#ffffff 75%)}
.about-copy{position:absolute;left:484px;top:2104px;width:610px;font-size:11.5px;line-height:21px;color:#555}
.about-copy h3{font-family:'Open Sans',Arial,sans-serif;color:var(--red);font-size:12.5px;font-weight:700;margin-bottom:6px}
.about-copy p{margin-bottom:0}
.about-copy .gap{margin-top:20px}

/* contact */
.contact-band{position:absolute;top:2400px;left:0;width:1200px;height:549px;background:var(--band)}
.field-label{position:absolute;font-size:12px;color:#555}
.field{position:absolute;height:32px;background:var(--white);border:1px solid #e2e2e2}
.submit{position:absolute;left:194px;top:2844px;width:276px;height:43px;background:var(--red);color:var(--white);
  font-family:'Raleway',Arial,sans-serif;font-weight:700;font-size:18px;text-align:center;line-height:43px;
  box-shadow:0 3px 0 #a5161b}
.callback{position:absolute;left:823px;top:2592px;width:270px;height:270px;border-radius:50%;background:#6a6a6a;
  border:10px solid #bdbdbd;text-align:center;color:#e9e9e9}
.callback p{position:absolute;top:106px;left:30px;width:190px;font-size:12.5px;line-height:19px}
.callback .cta{position:absolute;left:49px;top:178px;width:152px;height:34px;background:#1f1f1f;color:var(--white);
  font-size:11px;font-weight:700;line-height:34px}

/* footer */
.site-footer{position:absolute;top:2949px;left:0;width:1200px;height:76px;background:var(--footer)}
.site-footer small{position:absolute;left:110px;top:28px;font-size:11.5px;color:#aaa}
.foot-social{position:absolute;top:22px;width:32px;height:32px;border-radius:50%;border:2px solid #cfcfcf}
</style>
</head>
<body>

<header class="site-header">
  <div class="brand"><span class="brand-mark"></span><span class="brand-name">Harborlight Studio</span></div>
  <nav class="main-nav">
    <a class="active" style="left:548px">Home</a>
    <a style="left:630px">About</a>
    <a style="left:708px">Services</a>
    <a style="left:798px">Portfolio</a>
    <a style="left:892px">Case Studies</a>
    <a style="left:1015px">Contact Us</a>
  </nav>
  <span class="nav-underline"></span>
</header>

<section class="hero" aria-label="Hero"></section>
<div class="hero-photo" role="img" aria-label="Hands holding a tablet showing a fitness profile dashboard on a desk with a plant and a coffee cup"></div>
<h1 class="hero-title">Website Design Services</h1>
<p class="hero-sub">Our award-winning staff has years of experience providing Website Design services for business-class websites.</p>

<h2 class="section-title" style="top:678px">Our Services</h2>
<p class="section-intro" style="top:740px">Lorem ipsum dolor sit amet, consectetur adipiscing elit, sed do eiusmod tempor incididunt ut labore et dolore magna aliqua. Ut enim ad minim veniam, quis nostrud exercitation ullamco laboris nisi ut aliquip ex ea commodo consequat duis aute irure dolor in reprehenderit in voluptate.</p>

<div class="service" style="left:86px">
  <div class="badge red">
    <svg width="64" height="64" viewBox="0 0 64 64"><circle cx="32" cy="32" r="28" fill="none" stroke="#fff" stroke-width="3"/><path d="M32 32V8A24 24 0 0 1 56 32Z" fill="#fff"/><path d="M32 32L56 32A24 24 0 0 1 20 53Z" fill="#fff" opacity=".75"/></svg>
  </div>
  <h3>Website design</h3>
  <p>Lorem ipsum dolor sit amet, consectetur adipiscing elit, sed eiusmod tempor incididunt ut labore et dolore magna enim minim veniam.</p>
</div>
<div class="service" style="left:346px">
  <div class="badge grey">
    <svg width="60" height="60" viewBox="0 0 60 60" fill="none" stroke="#fff" stroke-width="6" stroke-linecap="round"><path d="M12 26A18 18 0 0 1 44 16"/><path d="M48 34A18 18 0 0 1 16 44"/><path d="M36 14L46 15L45 5" stroke-width="5"/><path d="M24 46L14 45L15 55" stroke-width="5"/></svg>
  </div>
  <h3>SEO</h3>
  <p>Lorem ipsum dolor sit amet, consectetur adipiscing elit, sed eiusmod tempor incididunt ut labore et dolore magna enim minim veniam.</p>
</div>
<div class="service" style="left:608px">
  <div class="badge red">
    <svg width="52" height="60" viewBox="0 0 52 60" fill="none" stroke="#fff" stroke-width="3"><rect x="4" y="8" width="44" height="50" rx="3"/><rect x="17" y="3" width="18" height="9" fill="#fff"/><path d="M12 24h4M21 24h19M12 34h4M21 34h19M12 44h4M21 44h19"/></svg>
  </div>
  <h3>Social Networking</h3>
  <p>Lorem ipsum dolor sit amet, consectetur adipiscing elit, sed eiusmod tempor incididunt ut labore et dolore magna enim minim veniam.</p>
</div>
<div class="service" style="left:868px">
  <div class="badge grey">
    <svg width="66" height="62" viewBox="0 0 66 62" fill="#fff"><circle cx="20" cy="8" r="5"/><circle cx="33" cy="6" r="5"/><circle cx="46" cy="8" r="5"/><circle cx="18" cy="26" r="6"/><circle cx="48" cy="26" r="6"/><rect x="11" y="34" width="14" height="26" rx="3"/><rect x="41" y="34" width="14" height="26" rx="3"/><rect x="26" y="40" width="14" height="4"/></svg>
  </div>
  <h3>App development</h3>
  <p>Lorem ipsum dolor sit amet, consectetur adipiscing elit, sed eiusmod tempor incididunt ut labore et dolore magna enim minim veniam.</p>
</div>

<section class="work-band" aria-label="Our Work"></section>
<h2 class="section-title" style="top:1212px">Our Work</h2>
<p class="section-intro" style="top:1273px">Lorem ipsum dolor sit amet, consectetur adipiscing elit, sed do eiusmod tempor incididunt ut labore et dolore magna aliqua. Ut enim ad minim veniam, quis nostrud exercitation ullamco laboris nisi ut aliquip ex ea commodo consequat duis aute irure dolor in reprehenderit in voluptate.</p>

<article class="work-card" style="left:200px">
  <div class="shot" role="img" aria-label="Smartphone resting on a laptop keyboard" style="background:linear-gradient(150deg,#c9d9e6,#7f99ad 60%,#34495b)"></div>
  <div class="label">Linden Advisory Group</div>
  <p>Lorem ipsum dolor sit amet is a consectetur adipiscing elit sed do eiusmod incididunt ut labore dolore magna aliqua enim minim veniam, quis nostrud exercitation.</p>
  <div class="share"><span class="s1"></span><span class="s2"></span><span class="s3"></span><span class="s4"></span></div>
</article>
<article class="work-card" style="left:476px">
  <div class="shot" role="img" aria-label="Hand holding a phone with colourful app tiles outdoors" style="background:linear-gradient(150deg,#b9cf7a,#d9a55a 55%,#6b5a3e)"></div>
  <div class="label">Prairie Smokehouse</div>
  <p>Lorem ipsum dolor sit amet is a consectetur adipiscing elit sed do eiusmod incididunt ut labore dolore magna aliqua enim minim veniam, quis nostrud exercitation.</p>
  <div class="share"><span class="s1"></span><span class="s2"></span><span class="s3"></span><span class="s4"></span></div>
</article>
<article class="work-card" style="left:752px">
  <div class="shot" role="img" aria-label="Businessman with a glowing network globe above a tablet" style="background:radial-gradient(circle at 55% 35%,#4a7fd0 0%,#1d3a78 45%,#0b1634 100%)"></div>
  <div class="label featured">Fernbrook Nursery</div>
  <p>Lorem ipsum dolor sit amet is a consectetur adipiscing elit sed do eiusmod incididunt ut labore dolore magna aliqua enim minim veniam, quis nostrud exercitation.</p>
  <div class="share"><span class="s1"></span><span class="s2"></span><span class="s3"></span><span class="s4"></span></div>
</article>

<span class="about-stem"></span>
<div class="about-badge">
  <svg width="62" height="50" viewBox="0 0 62 50" fill="#fff"><circle cx="31" cy="10" r="8"/><path d="M17 48V32a14 12 0 0 1 28 0V48Z"/><circle cx="12" cy="16" r="6"/><path d="M1 44V32a11 9 0 0 1 15-8V44Z"/><circle cx="50" cy="16" r="6"/><path d="M61 44V32a11 9 0 0 0-15-8V44Z"/></svg>
</div>
<h2 class="section-title" style="top:2010px">About Us</h2>
<div class="about-visual" role="img" aria-label="Blue and white 3D bar chart with a pie chart on paper reports"></div>
<div class="about-copy">
  <h3>Kansas City Website Design - Harborlight Studio, L.L.C.</h3>
  <p>Do you want us to tell you the truth about Harborlight Studio, or tell you what you want to hear?</p>
  <p>Just the facts then: Harborlight Studio invented the Internet. It is even named after us.</p>
  <p>Ok... Truth is, Harborlight Studio has a long history of building high performance Websites.</p>
  <p class="gap">Since 1998 Harborlight Studio has developed application-rich virtual marketplaces, providing organizations the tools to interact with their customers and prospects. Harborlight Studio didn't invent the Internet, but Harborlight Studio has grown-up with it.</p>
  <p class="gap">If you wanted to hear that Harborlight Studio created a 12-Step Marketing Process and Flow Chart procedure, Sorry. When we find two clients who fit in the same process, perhaps we will create one. Until then, know that Harborlight Studio has the experience, agility, and talent required to meet our client's needs.</p>
</div>

<section class="contact-band" aria-label="Contact Us"></section>
<h2 class="section-title" style="top:2437px">Contact Us</h2>
<p class="section-intro" style="top:2497px">Lorem ipsum dolor sit amet, consectetur adipiscing elit, sed do eiusmod tempor incididunt ut labore et dolore magna aliqua. Ut enim ad minim veniam, quis nostrud exercitation ullamco laboris nisi ut aliquip ex ea commodo consequat duis aute irure dolor in reprehenderit in voluptate.</p>

<span class="field-label" style="left:110px;top:2587px">First Name :</span><span class="field" style="left:192px;top:2580px;width:232px"></span>
<span class="field-label" style="left:462px;top:2587px">Last Name :</span><span class="field" style="left:541px;top:2580px;width:232px"></span>
<span class="field-label" style="left:110px;top:2632px">E-mail :</span><span class="field" style="left:192px;top:2625px;width:232px"></span>
<span class="field-label" style="left:462px;top:2632px">Phone :</span><span class="field" style="left:541px;top:2625px;width:232px"></span>
<span class="field-label" style="left:110px;top:2677px">Company :</span><span class="field" style="left:192px;top:2670px;width:232px"></span>
<span class="field-label" style="left:462px;top:2677px">Business :</span><span class="field" style="left:541px;top:2670px;width:232px"></span>
<span class="field-label" style="left:110px;top:2722px">Message :</span><span class="field" style="left:192px;top:2718px;width:581px;height:102px"></span>
<div class="submit">SUBMIT DETAILS</div>

<div class="callback">
  <svg class="abs" style="left:106px;top:24px" width="58" height="70" viewBox="0 0 58 70" fill="#ddd"><circle cx="29" cy="22" r="16"/><path d="M2 70a27 22 0 0 1 54 0Z"/><path d="M9 24a20 20 0 0 1 40 0" fill="none" stroke="#ddd" stroke-width="4"/></svg>
  <p>Do You have any further Questions? No Worries. We will call you.</p>
  <div class="cta">REQUEST CALL BACK</div>
</div>

<footer class="site-footer">
  <small>Copyrights © 2014. Harborlight Studio . All Rights Reserved</small>
  <span class="foot-social" style="left:944px"></span>
  <span class="foot-social" style="left:982px"></span>
  <span class="foot-social" style="left:1021px"></span>
  <span class="foot-social" style="left:1059px"></span>
</footer>

</body>
</html>
```